DeSIGN OF CARDS AND STATIONARY
MIRELLO VANTURA LAW
DeSIGN OF CARDS AND STATIONARY - Law
Creative Brief
Cutting-Edge
Rosalind Mirello Vantura
Criminal ATTORNEY
no address on the. card
rosalind@mirellovanturalaw.example
www.mirellovanturalaw.example
I. already. have. a logo I want to use
front of the. card will be the logo and name I send you. and in the back of the card will be. my info with logo. NEED TO ATTACH THE LOGO I JUST GOT.

```html
<!DOCTYPE html>
<html lang="en">
<head>
<meta charset="utf-8">
<title>Mirello Vantura Law — Business Cards</title>
<link rel="stylesheet" href="https://fonts.googleapis.com/css2?family=Montserrat:wght@400;500;600&display=swap">
<style>
  :root {
    --navy: #1f2152;
    --navy-deep: #171940;
    --slate: #7189ad;
    --slate-soft: #a9b8cf;
    --paper: #ffffff;
    --ink: #2a2c55;
    --ground: #eceef1;
  }
  * { margin: 0; padding: 0; box-sizing: border-box; }
  html, body {
    width: 1200px; height: 951px; overflow: hidden;
    background: var(--ground);
    font-family: "Montserrat", Arial, sans-serif;
  }
  .canvas { position: relative; width: 1200px; height: 951px; }

  .card {
    position: absolute; width: 600px; height: 343px; overflow: hidden;
    background: var(--navy);
    box-shadow: 0 14px 30px rgba(20, 22, 60, 0.22);
  }
  .card-back { left: 110px; top: 90px; }
  .card-front { left: 490px; top: 510px; }

  .card-shape { position: absolute; inset: 0; }

  .brand { position: absolute; text-align: center; color: var(--slate-soft); }
  .brand-mark {
    display: block; margin: 0 auto 10px;
    width: 34px; height: 34px; border-radius: 50%;
    background: var(--slate);
  }
  .brand-name { display: block; font-weight: 500; letter-spacing: 0.32em; }
  .brand-sub { display: block; font-weight: 400; letter-spacing: 0.5em; margin-top: 6px; }

  .card-back .brand { left: 10px; width: 230px; top: 52px; }
  .card-back .brand-name { font-size: 11px; }
  .card-back .brand-sub { font-size: 8px; }

  .contact { position: absolute; left: 318px; top: 62px; color: var(--ink); }
  .contact-firm { font-size: 17px; font-weight: 500; letter-spacing: 0.06em; }
  .contact-role { font-size: 10px; font-weight: 500; letter-spacing: 0.14em; margin-top: 4px; }
  .contact-rule { width: 250px; height: 1px; background: var(--slate); margin: 12px 0 16px; }
  .contact-list { list-style: none; }
  .contact-item {
    display: flex; align-items: center; gap: 9px;
    font-size: 10.5px; letter-spacing: 0.04em; margin-bottom: 8px;
  }
  .contact-icon { width: 15px; height: 15px; flex: none; }

  .card-front .brand { left: 0; width: 100%; top: 118px; }
  .card-front .brand-mark { width: 46px; height: 46px; margin-bottom: 16px; }
  .card-front .brand-name { font-size: 20px; color: var(--paper); }
  .card-front .brand-sub { font-size: 11px; color: var(--slate-soft); margin-top: 10px; }
</style>
</head>
<body>
<main class="canvas">

  <section class="card card-back" aria-label="Business card, contact side">
    <svg class="card-shape" viewBox="0 0 600 343" width="600" height="343">
      <defs>
        <linearGradient id="gavelTone" x1="0" y1="0" x2="1" y2="1">
          <stop offset="0" stop-color="#3a3f72"/>
          <stop offset="1" stop-color="#1b1d47"/>
        </linearGradient>
      </defs>
      <rect x="0" y="180" width="250" height="163" fill="url(#gavelTone)" opacity="0.85"
            role="img" aria-label="Photograph of a judge's gavel on a sound block"/>
      <path d="M262,0 C212,90 218,250 300,343 L318,343 C240,250 232,90 280,0 Z" fill="var(--slate)"/>
      <path d="M280,0 L600,0 L600,343 L318,343 C240,250 232,90 280,0 Z" fill="var(--paper)"/>
    </svg>

    <div class="brand">
      <span class="brand-mark"></span>
      <span class="brand-name">MIRELLO VANTURA</span>
      <span class="brand-sub">LAW</span>
    </div>

    <div class="contact">
      <h1 class="contact-firm">MIRELLO VANTURA LAW</h1>
      <p class="contact-role">CRIMINAL ATTORNEY</p>
      <div class="contact-rule"></div>
      <ul class="contact-list">
        <li class="contact-item">
          <svg class="contact-icon" viewBox="0 0 16 16"><circle cx="8" cy="8" r="8" fill="var(--ink)"/><path d="M5.2,4 L6.6,4 L7.2,6 L6.3,6.8 C6.8,8 7.9,9.1 9.2,9.7 L10,8.8 L12,9.4 L12,10.8 C12,11.4 11.5,11.8 10.9,11.7 C7.6,11.3 4.7,8.4 4.3,5.1 C4.2,4.5 4.6,4 5.2,4 Z" fill="var(--paper)"/></svg>
          <span>305-555-0142</span>
        </li>
        <li class="contact-item">
          <svg class="contact-icon" viewBox="0 0 16 16"><circle cx="8" cy="8" r="8" fill="var(--ink)"/><rect x="4" y="5" width="8" height="6" fill="none" stroke="var(--paper)" stroke-width="1"/><path d="M4,5 L8,8.3 L12,5" fill="none" stroke="var(--paper)" stroke-width="1"/></svg>
          <span>rosalind@mirellovanturalaw.example</span>
        </li>
        <li class="contact-item">
          <svg class="contact-icon" viewBox="0 0 16 16"><circle cx="8" cy="8" r="8" fill="var(--ink)"/><circle cx="8" cy="8" r="4" fill="none" stroke="var(--paper)" stroke-width="1"/><path d="M4,8 L12,8 M8,4 C6.4,6 6.4,10 8,12 M8,4 C9.6,6 9.6,10 8,12" fill="none" stroke="var(--paper)" stroke-width="0.9"/></svg>
          <span>www.mirellovanturalaw.example</span>
        </li>
      </ul>
    </div>
  </section>

  <section class="card card-front" aria-label="Business card, logo side">
    <svg class="card-shape" viewBox="0 0 600 343" width="600" height="343" aria-hidden="true">
      <circle cx="300" cy="150" r="210" fill="none" stroke="var(--navy-deep)" stroke-width="46" opacity="0.55"/>
    </svg>
    <div class="brand">
      <span class="brand-mark"></span>
      <span class="brand-name">MIRELLO VANTURA</span>
      <span class="brand-sub">LAW</span>
    </div>
  </section>

</main>
</body>
</html>
```